New Website for IT Services Business

We need an uncoded web design for a new company based in Australia called "Falcon IT". We offer specialised point of sale (POS) support to the hospitality industry. We already support hundreds of cafes and restaurants. We are also about to launch and promote a range of new services with the offering of General IT Support being the most important. Other additional services to be offered are Falcon Vault Storage, reselling and supporting Corvel Shieldware and Trelmo Suite.

We have a logo design and our colour scheme is based on the logo with the addition of charcoal grey (see attached logos). We want the pages to reflect precision and efficiency with sharp characteristics. It must be professional but playful/fun elements are encouraged.

Our target audience is restaurant and cafe owners who are interested in finding high quality POS and IT support for their business.

The main call to action on the home page should be either 'Let's Meet For Coffee!' or 'Find out more (by completing a form)'. If you are unsure about what the general text should say then you can use 'Lorem Ipsum' where required.

The site must be viewable at different resolutions and on smart phones and tablets.

The website structure will be quite simple. We require:
- one impressive landing page. Visitors will quickly determine our services and that we provide a very high level of service while also offering value for money. Obviously a clear list of links (however/wherever you like) to the other pages.
- Simple pages with a similar layout for the following:
- Services - "POS & IT Support for the Hospitality Industry" being the main one. With complementary services also listed. Another call to action on this page with the option of 'Let's Meet For Coffee' or a "More information/Pricing" form to be completed by the visitor.
- Products - will be a small online storefront for a few simple products.
- About - Business background. 2x Directors with a photo and brief Bio.
- Downloads - A list of free files to download. Includes remote access client software.
- Contact Us - Mailing address, Email addresses and Support phone number.

Please feel free to ask any questions about the design. I will assist as much as possible.

Thank you for viewing. We promise to give constructive feedback to every person who submits a design. Thank you so much.

Target Market(s)

Restaurant and Cafe owners.

Industry/Entity Type

Hospitality

Requirements
Must have
• - Viewable on different resolutions and on smart phones and tablets.
- Clear call to action of EITHER 'Let's Meet For Coffee' or a "More information/Pricing" form to be completed by the visitor.

```html
<!DOCTYPE html>
<html lang="en">
<head>
<meta charset="utf-8">
<title>Falcon IT – Home</title>
<link rel="stylesheet" href="https://fonts.googleapis.com/css2?family=Kurale&family=Noto+Sans:wght@400;700&display=swap">
<style>
  :root {
    --red: #c41e30;
    --red-dark: #8e1422;
    --charcoal: #2b2b2d;
    --panel: #eeeced;
    --tab-grey: #cccccc;
    --text-grey: #555555;
    --field-border: #b5b5b5;
    --white: #ffffff;
  }
  * { box-sizing: border-box; margin: 0; padding: 0; }
  html, body { width: 1200px; height: 918px; overflow: hidden; background: var(--white); }
  body { position: relative; font-family: "Noto Sans", Verdana, sans-serif; color: var(--text-grey); }

  .brand { position: absolute; left: 365px; top: 21px; height: 112px; display: flex; align-items: center; gap: 22px; }
  .brand-mark { width: 108px; height: 108px; border-radius: 50%; background: var(--red); }
  .brand-name { font-family: "Noto Sans", sans-serif; font-weight: 700; font-size: 74px; color: var(--charcoal); letter-spacing: -1px; }

  .top-band { position: absolute; left: 0; top: 164px; width: 1200px; height: 10px; background: var(--red); }

  .main-nav a {
    position: absolute; top: 174px; height: 54px;
    display: flex; align-items: center; justify-content: center;
    font-family: "Kurale", serif; font-size: 29px; color: var(--red);
    text-decoration: none; background: var(--tab-grey);
    border-radius: 0 0 10px 10px;
  }
  .main-nav a.is-current { background: var(--red); color: #f3dde0; }

  .feature-photo { position: absolute; top: 294px; width: 266px; height: 178px; border: 3px solid #4a4a4a; border-radius: 4px; }
  .photo-lounge { left: 30px; background: linear-gradient(135deg, #2d2119 0%, #6a4a33 40%, #c8b9a6 62%, #3b2a1e 100%); }
  .photo-bar { left: 354px; background: linear-gradient(160deg, #1c1a18 0%, #4d3d1f 35%, #b08a3a 55%, #2a2219 100%); }

  .feature-card { position: absolute; top: 472px; width: 265px; height: 286px; background: var(--panel); padding: 18px 4px 0 4px; }
  .feature-card p { font-size: 17px; line-height: 20.6px; color: var(--text-grey); }
  .card-one { left: 32px; }
  .card-two { left: 355px; }

  .find-more {
    position: absolute; left: 149px; top: 240px; width: 95px; height: 26px;
    background: linear-gradient(#f4f4f4, #c9c9c9); border-radius: 3px;
    font-size: 17px; color: var(--red); text-align: center; line-height: 25px;
    box-shadow: 0 1px 2px rgba(0,0,0,0.3);
  }

  .column-divider { position: absolute; left: 325px; top: 292px; width: 2px; height: 466px; background: #9a9a9a; }

  .coffee-panel { position: absolute; left: 791px; top: 295px; width: 374px; height: 463px; background: var(--panel); }
  .coffee-title { position: absolute; left: 0; top: 15px; width: 374px; text-align: center; font-size: 32px; color: var(--red); white-space: nowrap; }
  .enquiry-title { position: absolute; left: 33px; top: 120px; font-size: 28px; color: var(--red); }
  .field { position: absolute; left: 36px; width: 308px; border: 2px solid var(--field-border); background: var(--panel); font-size: 11px; color: #444; padding: 1px 3px; }
  .field-name { top: 174px; height: 29px; }
  .field-email { top: 212px; height: 28px; }
  .field-subject { top: 249px; height: 30px; }
  .field-message { top: 286px; height: 116px; }
  .field-message .scrollbar { position: absolute; right: 0; top: 0; width: 12px; height: 100%; background: #dcdcdc; border-left: 1px solid #bbb; }
  .send-button {
    position: absolute; left: 36px; top: 412px; width: 67px; height: 25px;
    background: linear-gradient(#f4f4f4, #bdbdbd); border-radius: 3px;
    font-size: 14px; color: #444; text-align: center; line-height: 24px;
  }

  .site-footer { position: absolute; left: 0; top: 826px; width: 1200px; height: 92px; background: var(--red); }
  .footer-glow { position: absolute; left: 20px; top: 0; width: 140px; height: 92px; background: radial-gradient(circle at 60px 46px, #e8303f 0%, rgba(196,30,48,0) 70%); }
  .footer-mark { position: absolute; left: 60px; top: 26px; width: 40px; height: 40px; border-radius: 50%; background: var(--white); }
  .copyright { position: absolute; left: 115px; top: 36px; font-size: 15px; color: var(--white); }
  .footer-nav a { position: absolute; top: 32px; font-size: 20px; color: var(--white); text-decoration: none; }
  .footer-rule { position: absolute; top: 24px; width: 3px; height: 42px; background: var(--red-dark); }
</style>
</head>
<body>
  <header>
    <div class="brand">
      <span class="brand-mark"></span>
      <span class="brand-name">Falcon IT</span>
    </div>
    <div class="top-band"></div>
    <nav class="main-nav">
      <a class="is-current" href="#" style="left:32px;width:177px">Home</a>
      <a href="#" style="left:220px;width:178px">Services</a>
      <a href="#" style="left:409px;width:179px">Produts</a>
      <a href="#" style="left:600px;width:180px">About</a>
      <a href="#" style="left:792px;width:182px">Downloads</a>
      <a href="#" style="left:982px;width:184px">Contact us</a>
    </nav>
  </header>

  <main>
    <div class="feature-photo photo-lounge" role="img" aria-label="Photo of a modern restaurant lounge with a suspended fireplace"></div>
    <div class="feature-card card-one">
      <p>I'm a paragraph. Click here to add your own text and edit me. It’s easy. Just click “Edit Text” or double click me and you can start adding your own content and make changes to the font. Feel free to drag and drop me any-where you like on your page.</p>
      <span class="find-more">find more</span>
    </div>

    <div class="column-divider"></div>

    <div class="feature-photo photo-bar" role="img" aria-label="Photo of a dimly lit bar counter with golden shelves and bar stools"></div>
    <div class="feature-card card-two">
      <p>I'm a paragraph. Click here to add your own text and edit me. It’s easy. Just click “Edit Text” or double click me and you can start adding your own content and make changes to the font. Feel free to drag and drop me any-where you like on your page.</p>
      <span class="find-more">find more</span>
    </div>

    <section class="coffee-panel">
      <h2 class="coffee-title" style="font-weight:400">'Let's Meet For Coffee!'</h2>
      <h3 class="enquiry-title" style="font-weight:400">Find out more</h3>
      <div class="field field-name">name</div>
      <div class="field field-email">email</div>
      <div class="field field-subject">subject</div>
      <div class="field field-message">message<span class="scrollbar"></span></div>
      <div class="send-button">Send</div>
    </section>
  </main>

  <footer class="site-footer">
    <div class="footer-glow"></div>
    <span class="footer-mark"></span>
    <span class="copyright">copyright Falcon IT</span>
    <nav class="footer-nav">
      <span class="footer-rule" style="left:700px"></span>
      <a href="#" style="left:714px">About Falcon IT</a>
      <span class="footer-rule" style="left:881px"></span>
      <a href="#" style="left:894px">Terms of use</a>
      <span class="footer-rule" style="left:1047px"></span>
      <a href="#" style="left:1062px">Privacy</a>
    </nav>
  </footer>
</body>
</html>
```